Conservative, Modern and Sharp Builder Business card

Hi there,
We would like to update our existing business card.
I have attached photos of existing business card, logo and van sign.

I would like the business card to also list what we do :
Renovation • New Build • Alteration
Extension • Bathroom • Maintenance.(Seperated by dots)

Contact number : 021 0483 0752
(With that exact spacing)

Ideally when people looking from about 2-3 metres, they know that it is a builder’s business card

Open to suggestions on fonts, layout, style of business card

PLEASE ONLY SUBMIT YOUR BEST OR MAX 3 DESIGNS FOR EACH DESIGNER

Thanks

Construction. Renovation

Details should be the same as the existing card. And addition of what we do.

• The new business card must not have the same layout as our existing one. Thanks

```html
<!DOCTYPE html>
<html lang="en">
<head>
<meta charset="utf-8">
<title>Keelstone – Business Card</title>
<link href="https://fonts.googleapis.com/css2?family=Inter:wght@400;600;700&family=Source+Sans+3:wght@700&display=swap" rel="stylesheet">
<style>
  :root {
    --backdrop: #9a9a9a;
    --card-dark: #121212;
    --card-light: #ffffff;
    --ink: #111111;
    --ink-soft: #4a4a4a;
    --ink-muted: #555555;
    --reverse: #ececec;
  }
  * { margin: 0; padding: 0; box-sizing: border-box; }
  html, body { width: 1200px; height: 588px; overflow: hidden; }
  body {
    background: var(--backdrop);
    position: relative;
    font-family: "Inter", Arial, sans-serif;
  }
  .card {
    position: absolute;
    top: 142px;
    width: 487px;
    height: 287px;
  }
  .card--front { left: 87px; background: var(--card-dark); }
  .card--back { left: 622px; background: var(--card-light); color: var(--ink); }

  .brand-name {
    font-family: "Source Sans 3", Arial, sans-serif;
    font-weight: 700;
    letter-spacing: -0.5px;
    white-space: nowrap;
  }
  .card--front .brand-name {
    position: absolute;
    left: 0; right: 0;
    top: 112px;
    text-align: center;
    font-size: 56px;
    line-height: 1;
    color: var(--reverse);
  }
  .card--back .brand-name {
    position: absolute;
    left: 30px;
    width: 196px;
    top: 112px;
    text-align: center;
    font-size: 38px;
    line-height: 1;
    color: var(--ink);
  }
  .divider {
    position: absolute;
    left: 246px;
    top: 75px;
    width: 1.5px;
    height: 118px;
    background: var(--ink);
  }
  .contact-block {
    position: absolute;
    left: 270px;
    top: 72px;
  }
  .person-name {
    font-weight: 700;
    font-size: 18px;
    letter-spacing: 0.2px;
    line-height: 22px;
  }
  .person-role {
    font-size: 13px;
    color: var(--ink-soft);
    line-height: 18px;
  }
  .contact-list {
    list-style: none;
    margin-top: 12px;
  }
  .contact-list li {
    display: flex;
    align-items: center;
    gap: 6px;
    height: 18.5px;
    font-size: 13px;
    color: var(--ink-soft);
  }
  .contact-list li.phone { font-weight: 700; font-size: 14px; color: var(--ink); }
  .contact-list svg { width: 11px; height: 11px; flex: none; }
  .services {
    position: absolute;
    left: 0; right: 0;
    top: 238px;
    text-align: center;
    font-size: 13px;
    line-height: 17.5px;
    color: var(--ink-muted);
  }
</style>
</head>
<body>
  <section class="card card--front">
    <div class="brand-name">Keelstone</div>
  </section>

  <section class="card card--back">
    <div class="brand-name">Keelstone</div>
    <div class="divider"></div>
    <div class="contact-block">
      <div class="person-name">TOMAS HAVILI</div>
      <div class="person-role">Residential Builder</div>
      <ul class="contact-list">
        <li class="phone">
          <svg viewBox="0 0 24 24" aria-hidden="true"><path fill="#111" d="M6.6 10.8a15.1 15.1 0 0 0 6.6 6.6l2.2-2.2c.3-.3.7-.4 1-.2 1.1.4 2.3.6 3.6.6.6 0 1 .4 1 1V20c0 .6-.4 1-1 1A17 17 0 0 1 3 4c0-.6.4-1 1-1h3.5c.6 0 1 .4 1 1 0 1.3.2 2.5.6 3.6.1.3 0 .7-.2 1l-2.3 2.2z"/></svg>
          021 0483 0752
        </li>
        <li>
          <svg viewBox="0 0 24 24" aria-hidden="true"><path fill="#111" d="M2 5h20v14H2z"/><path fill="none" stroke="#fff" stroke-width="1.8" d="M2.5 5.5l9.5 7 9.5-7"/></svg>
          hello@keelstone.co.nz
        </li>
        <li>
          <svg viewBox="0 0 24 24" aria-hidden="true"><circle cx="12" cy="12" r="10" fill="#111"/><path fill="none" stroke="#fff" stroke-width="1.4" d="M2 12h20M12 2c3 3 3 17 0 20M12 2c-3 3-3 17 0 20"/></svg>
          www.Keelstone.co.nz
        </li>
        <li>
          <svg viewBox="0 0 24 24" aria-hidden="true"><rect x="3" y="3" width="18" height="18" rx="2" fill="none" stroke="#111" stroke-width="2.4"/></svg>
          Keelstone.build
        </li>
      </ul>
    </div>
    <p class="services">
      Renovation • New Build • Alteration<br>
      Extension • Bathroom • Maintenance
    </p>
  </section>
</body>
</html>
```